I need a shopify website for a beauty brand that i am starting. The name of the brand is called "Velna Beauty" i need the website to have a "Sleek Sexy And Mordern Design" preferable with a "Black Colour Scheme" i need the shopify store to be "Integrated With Instagram and Facebook" (@VelnaBeauty on Instagram and Velna Beauty On Facebook) ... I Also need to be able to "Easily to upload future products" (as ive only got three products at the moment) and i will also need to be "Able to capture emails to use for email marketing in the future as the brand grows "

```html
<!DOCTYPE html>
<html lang="en">
<head>
<meta charset="utf-8">
<title>Velna Beauty</title>
<link href="https://fonts.googleapis.com/css2?family=Allura&family=Merriweather:wght@300;400;700;900&display=swap" rel="stylesheet">
<style>
:root{
  --black:#000;
  --ink:#0a0a0a;
  --white:#fff;
  --muted:#bdbdbd;
  --grey:#8d8d8d;
  --tag:#c9c9c9;
  --line:#3a3a3a;
  --serif:'Merriweather', Georgia, serif;
  --script:'Allura', cursive;
}
*{box-sizing:border-box;margin:0;padding:0}
html,body{width:1200px;height:4392px;overflow:hidden;background:var(--black)}
body{position:relative;font-family:var(--serif);color:var(--white)}
.abs{position:absolute}
.center{left:0;width:1200px;text-align:center}

/* header */
.brand{left:500px;top:34px;width:200px;text-align:center;font:700 26px/1 var(--serif);letter-spacing:.5px;z-index:3}
.brand small{display:block;font-size:10px;letter-spacing:3px;margin-top:6px;font-weight:400}
.icons{left:912px;top:50px;display:flex;gap:18px;z-index:3}
.nav{top:116px;left:0;width:1200px;z-index:3;font-size:14px}
.nav a{position:absolute;color:var(--white);text-decoration:none}
.nav a.active{color:var(--muted)}

/* hero */
.hero-photo{left:0;top:150px;width:720px;height:600px;background:radial-gradient(ellipse at 45% 35%,#9b6a52 0%,#4a2c22 35%,#140c0a 70%,#000 100%)}
.script{font-family:var(--script);color:#d8d8d8;font-weight:400}
.hero-script{left:776px;top:315px;font-size:82px}
.hero-title{left:706px;top:412px;font:700 60px/1 var(--serif);letter-spacing:1px}
.dots{display:flex;gap:9px}
.dot{width:12px;height:12px;border-radius:50%;background:#8a8a8a}
.dot.on{background:var(--white)}

/* section heads */
.kicker{font-size:58px;line-height:1}
.heading{font:700 33px/1 var(--serif);letter-spacing:.5px}

/* products */
.card{width:235px;height:262px;background:var(--white);border-radius:28px 4px 28px 4px;overflow:hidden}
.card .photo{position:absolute;left:28px;top:30px;width:180px;height:170px;border-radius:8px;background:linear-gradient(160deg,#f3f3f3,#cfcfcf)}
.card .photo.dark{background:radial-gradient(circle at 50% 55%,#5a2f2b 0%,#1b1b1b 45%,#eee 46%,#f4f4f4 100%)}
.card .stars{position:absolute;left:16px;bottom:16px;display:flex;gap:2px}
.tag{position:absolute;right:4px;top:4px;width:86px;height:26px;background:var(--tag);color:#111;font-size:15px;line-height:26px;text-align:center}
.pname{font:700 17px/1 var(--serif);white-space:nowrap}
.pdesc{font-size:12px;line-height:17px;width:230px}
.price{font:300 24px/1 var(--serif);letter-spacing:-1px}

/* about */
.about-photo{left:512px;top:1398px;width:688px;height:438px;background:linear-gradient(90deg,#000 0%,#3a2418 20%,#b07a52 55%,#d9a47a 80%,#c89069 100%)}
.about-p{font-size:14px;line-height:19px;width:470px}
.btn{border:2px solid var(--white);border-radius:6px 0 6px 0;font:700 16px/38px var(--serif);text-align:center;color:var(--white)}

/* blog */
.blog-card{width:483px;height:307px;background:var(--white);border-radius:44px 4px 44px 4px;overflow:hidden;box-shadow:inset 0 -8px 14px rgba(0,0,0,.18)}
.blog-card .photo{position:absolute;left:40px;top:30px;width:403px;height:240px;border-radius:8px;background:linear-gradient(120deg,#1d1d1d,#5a5050 40%,#e6e6e6 70%,#f2f2f2)}
.blog-title{font:700 19px/1 var(--serif);color:#9a9a9a}
.blog-p{font-size:14px;line-height:20px;width:470px}

/* testimonials */
.testi-bg{left:0;top:2571px;width:1200px;height:438px;background:linear-gradient(100deg,#2a2523 0%,#5b504a 40%,#3a332f 70%,#1c1917 100%)}
.testi-photo{left:172px;top:2719px;width:234px;height:232px;border:3px solid var(--white);border-radius:0 0 38px 0;background:linear-gradient(150deg,#7a5236,#c79a6c 45%,#a2211c 80%)}
.testi-name{font:700 31px/1 var(--serif)}
.testi-p{font-size:14.5px;line-height:19px;width:570px}

/* instagram */
.insta{width:218px;height:220px;border-radius:28px 4px 28px 4px;overflow:hidden}
.insta.person{background:linear-gradient(160deg,#e9e2dc,#6a4433 50%,#2a1a14)}
.insta.bottle{background:radial-gradient(circle at 50% 55%,#3a2624,#161616 40%,#fff 41%)}
.insta.lash{background:linear-gradient(160deg,#fff,#e6e6e6)}

/* badges */
.badge{width:124px;height:78px;border:2px solid #cfcfcf;border-radius:4px}
.badge.round{border-radius:40px}

/* footer */
.f-title{font:400 17px/1 var(--serif);color:#d0d0d0}
.f-link{font-size:14px;color:var(--white)}
.datebox{width:51px;height:58px;border:2px solid var(--white);text-align:center;font:700 19px/1 var(--serif);padding-top:7px}
.datebox span{display:block;font-size:11px;font-weight:400;margin-top:8px}
.post-t{font:700 14px/1 var(--serif)}
.post-m{font-size:11px;color:#cfcfcf}
.input{left:864px;top:4182px;width:296px;height:41px;background:var(--white);color:#888;font-size:13px;line-height:41px;padding-left:14px}
.send{left:1104px;top:4186px;width:52px;height:33px;background:var(--black)}
.social{width:26px;height:26px;border:2px solid var(--white);border-radius:5px}
.rule{left:40px;top:4343px;width:1120px;height:1px;background:var(--line)}
</style>
</head>
<body>

<!-- header -->
<div class="abs brand">Velna Beauty<small>BEAUTY</small></div>
<div class="abs icons" aria-label="Account, wishlist and cart">
  <svg width="18" height="20" viewBox="0 0 18 20"><circle cx="9" cy="6" r="4.5" fill="#fff"/><path d="M1 19c0-5 3.5-7.5 8-7.5s8 2.5 8 7.5z" fill="#fff"/></svg>
  <svg width="20" height="18" viewBox="0 0 20 18"><path d="M10 17 2 9A4.7 4.7 0 0 1 10 3a4.7 4.7 0 0 1 8 6z" fill="#fff"/></svg>
  <svg width="22" height="20" viewBox="0 0 22 20"><path d="M1 2h4l3 11h10l3-8H7" fill="none" stroke="#fff" stroke-width="2.4"/><path d="M7 6h13l-2.6 7H9z" fill="#fff"/><circle cx="9" cy="17" r="2" fill="#fff"/><circle cx="17" cy="17" r="2" fill="#fff"/></svg>
</div>
<nav class="abs nav">
  <a class="active" style="left:355px">Home</a>
  <a style="left:438px">About</a>
  <a style="left:522px">Shop</a>
  <a style="left:598px">Reviews</a>
  <a style="left:696px">Gallery</a>
  <a style="left:788px">Contact</a>
</nav>

<!-- hero -->
<div class="abs hero-photo" role="img" aria-label="Portrait of a model with long dark hair holding a black feather"></div>
<div class="abs script hero-script">Welcome To</div>
<div class="abs hero-title">VELNA BEAUTY</div>
<div class="abs dots" style="left:900px;top:614px"><i class="dot on"></i><i class="dot"></i><i class="dot"></i></div>

<!-- new products -->
<div class="abs center script kicker" style="top:808px">Perfect Match</div>
<div class="abs center heading" style="top:878px">NEW PRODUCTS</div>

<div class="abs card" style="left:-136px;top:943px"><div class="photo" role="img" aria-label="Pair of false lashes"></div></div>
<div class="abs pname" style="left:-136px;top:1222px">PRODUCT NAME</div>
<div class="abs pdesc" style="left:-136px;top:1250px">It is a long established fact that a will be distracted by the readable .</div>

<div class="abs card" style="left:174px;top:943px"><div class="photo dark" role="img" aria-label="Black perfume bottle"></div>
  <div class="stars"><svg width="88" height="16" viewBox="0 0 88 16"><g fill="#111"><path id="s" d="M8 0l2.4 5.2 5.6.6-4.2 3.8 1.2 5.6L8 12.4 3 15.2l1.2-5.6L0 5.8l5.6-.6z"/><use href="#s" x="18"/><use href="#s" x="36"/><use href="#s" x="54"/><use href="#s" x="72"/></g></svg></div></div>
<div class="abs pname" style="left:174px;top:1222px">PRODUCT NAME</div>
<div class="abs pdesc" style="left:174px;top:1250px">It is a long established fact that a will be distracted by the readable .</div>
<div class="abs price" style="left:172px;top:1297px">$12.00</div>

<div class="abs card" style="left:484px;top:943px"><div class="photo" role="img" aria-label="Pair of false lashes"></div><div class="tag">10% OFF</div>
  <div class="stars"><svg width="88" height="16" viewBox="0 0 88 16"><g fill="#111"><use href="#s"/><use href="#s" x="18"/><use href="#s" x="36"/><use href="#s" x="54"/><use href="#s" x="72"/></g></svg></div></div>
<div class="abs pname" style="left:484px;top:1222px">PRODUCT NAME</div>
<div class="abs pdesc" style="left:484px;top:1250px">It is a long established fact that a will be distracted by the readable .</div>
<div class="abs price" style="left:482px;top:1297px">$22.00</div>

<div class="abs card" style="left:793px;top:943px"><div class="photo" role="img" aria-label="Gift box set with lashes and perfume"></div>
  <div class="stars"><svg width="88" height="16" viewBox="0 0 88 16"><g fill="#111"><use href="#s"/><use href="#s" x="18"/><use href="#s" x="36"/><use href="#s" x="54"/></g><use href="#s" x="72" fill="none" stroke="#111"/></svg></div></div>
<div class="abs pname" style="left:793px;top:1222px">PRODUCT NAME</div>
<div class="abs pdesc" style="left:793px;top:1250px">It is a long established fact that a will be distracted by the readable .</div>
<div class="abs price" style="left:791px;top:1297px">$59.00</div>

<div class="abs card" style="left:1103px;top:943px"><div class="photo dark" role="img" aria-label="Black perfume bottle"></div>
  <div class="stars"><svg width="88" height="16" viewBox="0 0 88 16"><g fill="#111"><use href="#s"/><use href="#s" x="18"/><use href="#s" x="36"/><use href="#s" x="54"/><use href="#s" x="72"/></g></svg></div></div>
<div class="abs pname" style="left:1103px;top:1222px">PRODUCT NAME</div>
<div class="abs pdesc" style="left:1103px;top:1250px">It is a long established fact that a will be distracted by the readable .</div>
<div class="abs price" style="left:1101px;top:1297px">$15.00</div>

<!-- about -->
<div class="abs about-photo" role="img" aria-label="Close-up of an eye with golden shadow and long lashes"></div>
<div class="abs script" style="left:50px;top:1420px;font-size:56px">We Provide</div>
<div class="abs" style="left:51px;top:1482px;font:700 36px/1 var(--serif)">Welcome to Velna Beauty</div>
<p class="abs about-p" style="left:51px;top:1550px">Lorem Ipsum is simply dummy text of the printing and typesetting industry. Lorem Ipsum has been the industry's standard dummy &nbsp;text ever since the 1500s,</p>
<p class="abs about-p" style="left:51px;top:1625px">when an unknown printer took a galley of type and scrambled it to make a type specimen book. remaining essentially unchanged. It was popularised in the with theLorem Ipsum is simply dummy text of the printing and eentially unchanged.</p>
<div class="abs btn" style="left:51px;top:1742px;width:154px;height:41px">Read More</div>

<!-- blog -->
<div class="abs center script kicker" style="top:1912px">Latest News</div>
<div class="abs center heading" style="top:1974px">BLOG</div>
<div class="abs blog-card" style="left:80px;top:2039px"><div class="photo" role="img" aria-label="Perfume bottle beside a pair of false lashes"></div></div>
<div class="abs blog-title" style="left:80px;top:2362px">Lorem Ipsum is simply dummy text industry.</div>
<p class="abs blog-p" style="left:80px;top:2394px">It is a long established fact that a reader will be distracted by the readable content of a page when looking at its layout.</p>
<div class="abs blog-card" style="left:638px;top:2039px"><div class="photo" role="img" aria-label="Boxed gift set of lashes and perfume"></div></div>
<div class="abs blog-title" style="left:638px;top:2362px">Lorem Ipsum is simply dummy text industry.</div>
<p class="abs blog-p" style="left:638px;top:2394px">It is a long established fact that a reader will be distracted by the readable content of a page when looking at its layout.</p>
<div class="abs btn" style="left:523px;top:2453px;width:154px;height:41px">See More</div>

<!-- testimonials -->
<div class="abs testi-bg" role="img" aria-label="Soft background of a woman with closed eyes"></div>
<div class="abs center script kicker" style="top:2598px">Customers Feedbacks</div>
<div class="abs center heading" style="top:2662px">TESTIMONIALS</div>
<div class="abs testi-photo" role="img" aria-label="Portrait of a smiling customer with blonde hair"></div>
<div class="abs testi-name" style="left:479px;top:2748px">Mara Ellison</div>
<div class="abs script" style="left:481px;top:2786px;font-size:30px">London</div>
<p class="abs testi-p" style="left:479px;top:2842px">It is a long established fact that a reader will be distracted by the readable content of a page when looking at its layout. The point of using Lorem Ipsum is that it has a more-or-less normal distribution of letters.It is a long established fact that a reader will be distracted by the readable content of a page when looking at its layout.</p>
<div class="abs dots" style="left:572px;top:2959px"><i class="dot on"></i><i class="dot"></i><i class="dot"></i></div>

<!-- promotions -->
<div class="abs center script kicker" style="top:3084px">Great Quality</div>
<div class="abs center heading" style="top:3150px">LIMITED PROMOTIONS</div>

<div class="abs card" style="left:-136px;top:3216px"><div class="photo" role="img" aria-label="Pair of false lashes"></div><div class="tag">10% OFF</div></div>
<div class="abs pdesc" style="left:-136px;top:3520px">It is a long established fact that a will be distracted by the readable .</div>

<div class="abs card" style="left:174px;top:3216px"><div class="photo dark" role="img" aria-label="Black perfume bottle"></div>
  <div class="stars"><svg width="88" height="16" viewBox="0 0 88 16"><g fill="#111"><use href="#s"/><use href="#s" x="18"/><use href="#s" x="36"/><use href="#s" x="54"/><use href="#s" x="72"/></g></svg></div></div>
<div class="abs pname" style="left:174px;top:3495px">PRODUCT NAME</div>
<div class="abs pdesc" style="left:174px;top:3520px">It is a long established fact that a will be distracted by the readable .</div>
<div class="abs price" style="left:172px;top:3570px">$12.00</div>

<div class="abs card" style="left:484px;top:3216px"><div class="photo" role="img" aria-label="Pair of false lashes"></div><div class="tag">10% OFF</div>
  <div class="stars"><svg width="88" height="16" viewBox="0 0 88 16"><g fill="#111"><use href="#s"/><use href="#s" x="18"/><use href="#s" x="36"/><use href="#s" x="54"/><use href="#s" x="72"/></g></svg></div></div>
<div class="abs pname" style="left:484px;top:3495px">PRODUCT NAME</div>
<div class="abs pdesc" style="left:484px;top:3520px">It is a long established fact that a will be distracted by the readable .</div>
<div class="abs price" style="left:482px;top:3570px">$22.00</div>

<div class="abs card" style="left:793px;top:3216px"><div class="photo" role="img" aria-label="Gift box set with lashes and perfume"></div>
  <div class="stars"><svg width="88" height="16" viewBox="0 0 88 16"><g fill="#111"><use href="#s"/><use href="#s" x="18"/><use href="#s" x="36"/><use href="#s" x="54"/></g><use href="#s" x="72" fill="none" stroke="#111"/></svg></div></div>
<div class="abs pname" style="left:793px;top:3495px">PRODUCT NAME</div>
<div class="abs pdesc" style="left:793px;top:3520px">It is a long established fact that a will be distracted by the readable .</div>
<div class="abs price" style="left:791px;top:3570px">$59.00</div>

<div class="abs card" style="left:1103px;top:3216px"><div class="photo dark" role="img" aria-label="Black perfume bottle"></div>
  <div class="stars"><svg width="88" height="16" viewBox="0 0 88 16"><g fill="#111"><use href="#s"/><use href="#s" x="18"/><use href="#s" x="36"/><use href="#s" x="54"/><use href="#s" x="72"/></g></svg></div></div>
<div class="abs pname" style="left:1103px;top:3495px">PRODUCT NAME</div>
<div class="abs pdesc" style="left:1103px;top:3520px">It is a long established fact that a will be distracted by the readable .</div>
<div class="abs price" style="left:1101px;top:3570px">$15.00</div>

<!-- instagram -->
<div class="abs center heading" style="top:3662px">FOLLOW US ON INSTAGRAM</div>
<div class="abs insta person" style="left:126px;top:3725px" role="img" aria-label="Model wearing lashes"></div>
<div class="abs insta bottle" style="left:370px;top:3725px" role="img" aria-label="Black perfume bottle"></div>
<div class="abs insta person" style="left:614px;top:3725px;border:3px solid #fff" role="img" aria-label="Model wearing lashes, close-up"></div>
<div class="abs insta lash" style="left:856px;top:3725px" role="img" aria-label="Pair of false lashes"></div>

<!-- partner badges -->
<div class="abs badge round" style="left:106px;top:4032px"></div>
<div class="abs badge" style="left:277px;top:4040px;height:62px"></div>
<div class="abs badge round" style="left:450px;top:4032px"></div>
<div class="abs badge" style="left:620px;top:4040px;height:62px"></div>
<div class="abs badge round" style="left:796px;top:4032px"></div>
<div class="abs badge" style="left:965px;top:4040px;height:62px"></div>

<!-- footer -->
<div class="abs" style="left:75px;top:4168px;width:200px;text-align:center;font:700 26px/1 var(--serif)">Velna Beauty</div>
<p class="abs" style="left:25px;top:4242px;width:300px;text-align:center;font-size:13.5px;line-height:19px">Item ipsum dolor sit amet, consectetuer adipiscing elit, sed diam nonummy nibh euismod tincidunt ut laoreet dolore agna aliquam erat . wisi enim ad minim veniam, quis tation.</p>

<div class="abs f-title" style="left:390px;top:4150px">Useful links</div>
<div class="abs f-link" style="left:390px;top:4178px">Home</div>
<div class="abs f-link" style="left:390px;top:4205px">About</div>
<div class="abs f-link" style="left:390px;top:4231px">Shop</div>
<div class="abs f-link" style="left:390px;top:4258px">Reviews</div>
<div class="abs f-link" style="left:390px;top:4284px">Gallery</div>
<div class="abs f-link" style="left:390px;top:4311px">Contact</div>

<div class="abs f-title" style="left:557px;top:4150px">Resent Post</div>
<div class="abs datebox" style="left:559px;top:4191px">20<span>MAR</span></div>
<div class="abs post-t" style="left:628px;top:4198px">Blog title first</div>
<div class="abs post-m" style="left:628px;top:4224px">&#9679; By Admin &nbsp;&#9679; 28</div>
<div class="abs datebox" style="left:559px;top:4266px">10<span>MAY</span></div>
<div class="abs post-t" style="left:628px;top:4273px">Blog title first</div>
<div class="abs post-m" style="left:628px;top:4299px">&#9679; By Admin &nbsp;&#9679; 28</div>

<div class="abs f-title" style="left:864px;top:4150px">Newsletter</div>
<div class="abs input">Enter Your Email</div>
<div class="abs send"><svg width="52" height="33" viewBox="0 0 52 33"><path d="M16 17 36 8l-6 18-5-6z" fill="#fff"/></svg></div>
<div class="abs f-title" style="left:864px;top:4248px">Social Links</div>
<div class="abs" style="left:864px;top:4280px;display:flex;gap:14px">
  <i class="social"></i><i class="social"></i><i class="social"></i><i class="social"></i><i class="social"></i><i class="social"></i>
</div>

<div class="abs rule"></div>
<div class="abs center" style="top:4360px;font-size:15px;color:#cfcfcf">© 2020 Velna Beauty - All rights reserved. Privacy Policy.</div>

</body>
</html>
```